bryn calvo website design

An IT support and IT Security Company - just use dummy text for now for the design. Examples of sites we like the looks and feel of but need it more professional feel are like: www.quorvatech.uk.com , www.halvion.co.uk, www.truvexa.com/professional/, www.zul.com, www.mivlen.com,

Best to message me if you have any questions

Target Market(s)

small to medium UK based companies that require IT support services

Industry/Entity Type

It Company

Contact Information for Business Card

use dummy name, telephone and email for now, will provide details later.

Logo Text

bryn calvo (and then below the logo it should say "your IT, networks and security partner")

Coding

Coded - Design and coding required

Number of Pages Required

5+ page

Colors

Designer to choose colors to be used in the design.

Requirements
Must have
• must be professional, yet simple and clear that this is a serious IT support and IT security company.
Nice to have
• 1)The website homepage must have professional quality pictures of IT support or London city skyline or any picture that projects friendly business partners, professionalism and ready to serve.
• 2) Home page needs to include tabs for following pages 'Services' , 'About Us' , 'Contact Us' 'Home'
• 3) Website built customised using wordpress is ideal and easy for us to manage.
• more room for boxed options from homepage (with pic or image in background)
Should not have
• no checkout trolleys or payment options.

```html
<!DOCTYPE html>
<html lang="en">
<head>
<meta charset="utf-8">
<title>bryn calvo — IT Support &amp; IT Security</title>
<link href="https://fonts.googleapis.com/css2?family=Didact+Gothic&family=Montserrat:wght@500;600&display=swap" rel="stylesheet">
<style>
  :root{
    --navy:#2e2b5f;
    --navy-deep:#28265a;
    --button:#3c4468;
    --button-edge:#1f2440;
    --ink:#2f2c62;
    --text:#8c8c8c;
    --text-dark:#555;
    --panel:#f5f5f5;
    --white:#ffffff;
    --bar:#9b9b9b;
    --bar-text:#3a3a3a;
  }
  *{box-sizing:border-box;margin:0;padding:0}
  html,body{width:1200px;height:2612px;overflow:hidden;background:var(--white)}
  body{font-family:"Didact Gothic",sans-serif;color:var(--text);position:relative}
  .abs{position:absolute}

  /* header */
  .site-header{position:absolute;left:0;top:0;width:1200px;height:94px;background:var(--white)}
  .brand{position:absolute;left:78px;top:18px;display:flex;align-items:center;gap:12px}
  .brand-mark{width:26px;height:26px;background:var(--navy)}
  .brand-name{font-family:"Didact Gothic",sans-serif;font-size:38px;color:var(--navy);letter-spacing:.5px;line-height:1}
  .main-nav{position:absolute;top:36px;left:465px;display:flex;gap:0}
  .main-nav a{font-family:"Montserrat",sans-serif;font-weight:500;font-size:15px;color:#c4c4c4;text-decoration:none;letter-spacing:.5px;position:absolute;white-space:nowrap}
  .main-nav a.is-active{color:var(--ink)}
  .btn{display:inline-block;background:var(--button);color:var(--white);font-family:"Montserrat",sans-serif;font-weight:600;font-size:14px;letter-spacing:.5px;text-decoration:none;border:2px solid var(--button-edge);box-shadow:inset 0 0 0 1px #6a7093;text-align:center}
  .btn-connect{position:absolute;left:915px;top:27px;width:208px;height:40px;line-height:36px}

  /* hero */
  .hero{position:absolute;left:0;top:94px;width:1200px;height:584px;
    background:radial-gradient(ellipse at 50% 40%,#d9ecff 0%,#5d9ad6 14%,#1f4f86 32%,#0a1d36 58%,#02060d 100%)}

  /* about */
  .about{position:absolute;left:0;top:678px;width:1200px;height:337px;text-align:center}
  .section-title{font-family:"Didact Gothic",sans-serif;font-weight:400;color:var(--ink);font-size:38px;line-height:1}
  .about .section-title{position:absolute;left:0;width:1200px;top:65px}
  .about-text{position:absolute;left:135px;width:930px;top:122px;font-size:14.5px;line-height:25px;color:var(--text)}
  .btn-more{position:absolute;left:533px;top:242px;width:134px;height:40px;line-height:36px;font-size:13px}

  /* service panels */
  .service{position:absolute;left:0;width:1200px;height:417px;background:var(--panel);overflow:hidden}
  .service-support{top:1015px}
  .service-security{top:1432px}
  .service-photo{position:absolute;top:0;height:417px}
  .service-icon{position:absolute}
  .service-title{position:absolute;font-family:"Didact Gothic",sans-serif;color:var(--ink);font-size:34px;line-height:1}
  .service-text{position:absolute;width:420px;font-size:13.5px;line-height:23px;color:var(--text-dark)}

  /* blogs */
  .blogs .section-title{position:absolute;left:0;width:1200px;text-align:center;top:1910px}
  .blog-card{position:absolute;top:1978px;width:333px}
  .blog-image{width:333px;height:166px}
  .blog-date{position:absolute;left:0;top:179px;width:52px;height:56px;background:var(--navy);color:var(--white);text-align:center;font-size:18px;line-height:21px;padding-top:7px;box-shadow:inset 0 0 0 2px #5a5f86}
  .blog-title{position:absolute;left:63px;top:179px;width:270px;font-size:14.5px;line-height:19px;color:var(--ink)}
  .blog-excerpt{position:absolute;left:63px;top:226px;width:260px;font-size:13px;line-height:19px;color:#a3a3a3}

  /* footer */
  .site-footer{position:absolute;left:0;top:2295px;width:1200px;height:267px;background:var(--navy-deep);color:var(--white)}
  .footer-brand{position:absolute;left:0;width:470px;top:52px;display:flex;justify-content:center;align-items:center;gap:12px}
  .footer-brand .brand-mark{background:#d9d9e6}
  .footer-brand .brand-name{color:#e6e6f0}
  .footer-about{position:absolute;left:90px;width:290px;top:140px;text-align:center;font-size:13.5px;line-height:20px}
  .footer-heading{position:absolute;top:56px;font-size:17px;color:var(--white)}
  .contact-list{position:absolute;left:435px;top:96px;list-style:none;font-size:13.5px;line-height:20px}
  .contact-list li{position:absolute;left:0;width:300px;padding-left:35px;white-space:nowrap}
  .contact-list svg{position:absolute;left:0;top:1px}
  .subscribe-text{position:absolute;left:792px;top:93px;width:330px;font-size:13.5px;line-height:23px}
  .subscribe-form{position:absolute;left:790px;top:153px;width:333px;height:57px;display:flex}
  .subscribe-input{width:240px;height:57px;background:var(--white);border:none;padding-left:20px;font-family:"Didact Gothic",sans-serif;font-style:italic;font-size:13px;color:#999}
  .subscribe-button{width:93px;height:57px;background:var(--navy);color:var(--white);border:2px solid #5a5f86;font-family:"Montserrat",sans-serif;font-weight:600;font-size:15px}

  .legal-bar{position:absolute;left:0;top:2562px;width:1200px;height:50px;background:var(--bar);border-top:3px solid #c7c7c7}
  .legal-text{position:absolute;left:83px;top:16px;font-size:13px;color:var(--bar-text)}
  .legal-text strong{font-weight:400;color:#1f1f2e;font-size:15px}
  .social-links{position:absolute;right:78px;top:16px;display:flex;gap:18px}
  .social-links span{display:block;width:14px;height:14px;background:var(--navy)}
</style>
</head>
<body>

<header class="site-header">
  <a class="brand" href="#" aria-label="bryn calvo home">
    <span class="brand-mark"></span>
    <span class="brand-name">bryn calvo</span>
  </a>
  <nav class="main-nav">
    <a class="is-active" href="#" style="left:0">HOME</a>
    <a href="#" style="left:97px">ABOUT</a>
    <a href="#" style="left:203px">SERVICES</a>
    <a href="#" style="left:328px">CONTACT</a>
  </nav>
  <a class="btn btn-connect" href="#">SIGN UP TO CONNECT</a>
</header>

<section class="hero" role="img" aria-label="Glowing blue digital circuit tunnel with floating numbers and a padlock at the centre"></section>

<section class="about">
  <h1 class="section-title">About bryn calvo</h1>
  <p class="about-text">Lorem Ipsum is simply dummy text of the printing and typesetting industry. Lorem Ipsum has been the industry's standard dummy text ever since the 1500s, when an unknown printer took a galley of type and scrambled it to make a type specimen book. It has survived not only five centuries, but also the leap into electronic typesetting, remaining essentially unchanged. It was popularised in the 1960s with the release of Letraset sheets containing.</p>
  <a class="btn btn-more" href="#">READ MORE</a>
</section>

<section class="service service-support">
  <svg class="service-photo" style="left:0" width="660" height="417" role="img" aria-label="Smiling support agent on the phone at an office desk with a monitor">
    <defs>
      <linearGradient id="supportTone" x1="0" y1="0" x2="1" y2="1">
        <stop offset="0" stop-color="#b8b4a8"/>
        <stop offset=".5" stop-color="#6f8a96"/>
        <stop offset="1" stop-color="#3a3d44"/>
      </linearGradient>
    </defs>
    <polygon points="0,0 652,0 568,417 0,417" fill="url(#supportTone)"/>
    <polygon points="645,0 659,0 575,417 561,417" fill="var(--navy)"/>
  </svg>
  <svg class="service-icon" style="left:695px;top:70px" width="92" height="52" viewBox="0 0 92 52" fill="none" stroke="#666" stroke-width="2">
    <circle cx="18" cy="14" r="9"/>
    <path d="M4 44c2-12 26-12 28 0z"/>
    <rect x="34" y="12" width="50" height="34" rx="2"/>
    <line x1="34" y1="20" x2="84" y2="20"/>
    <line x1="42" y1="30" x2="76" y2="30"/>
    <line x1="42" y1="38" x2="66" y2="38"/>
  </svg>
  <h2 class="service-title" style="left:695px;top:150px">IT support</h2>
  <p class="service-text" style="left:695px;top:205px">Lorem Ipsum is simply dummy text of the printing and typesetting industry. Lorem Ipsum has been the industry's standard dummy text ever since the 1500s, when an unknown printer took a galley of type and scrambled it to make a type specimen book. It has survived not only five centuries, but also the leap into electronic typesetting.</p>
</section>

<section class="service service-security">
  <svg class="service-photo" style="left:550px" width="650" height="417" role="img" aria-label="Open laptop mounted in a server rack with blue lit equipment">
    <defs>
      <linearGradient id="securityTone" x1="0" y1="0" x2="1" y2="1">
        <stop offset="0" stop-color="#1a2350"/>
        <stop offset=".5" stop-color="#3d4a8a"/>
        <stop offset="1" stop-color="#0c1030"/>
      </linearGradient>
    </defs>
    <polygon points="12,0 650,0 650,417 92,417" fill="url(#securityTone)"/>
    <polygon points="5,0 19,0 99,417 85,417" fill="var(--navy)"/>
  </svg>
  <svg class="service-icon" style="left:78px;top:72px" width="52" height="52" viewBox="0 0 52 52" fill="none" stroke="#666" stroke-width="2">
    <rect x="16" y="18" width="20" height="18" rx="2"/>
    <path d="M20 18v-5a6 6 0 0 1 12 0v5"/>
    <line x1="26" y1="24" x2="26" y2="30"/>
    <path d="M16 22H4M16 32H4M36 22h12M36 32h12M22 36v12M30 36v12M22 8V2M30 8V2"/>
  </svg>
  <h2 class="service-title" style="left:78px;top:150px">IT security</h2>
  <p class="service-text" style="left:78px;top:206px">Lorem Ipsum is simply dummy text of the printing and typesetting industry. Lorem Ipsum has been the industry's standard dummy text ever since the 1500s, when an unknown printer took a galley of type and scrambled it to make a type specimen book. It has survived not only five centuries, but also the leap into electronic typesetting.</p>
</section>

<section class="blogs">
  <h2 class="section-title">Latest Blogs</h2>

  <article class="blog-card" style="left:78px">
    <div class="blog-image" role="img" aria-label="Person wearing a virtual reality headset at a desk with monitors" style="background:linear-gradient(135deg,#2c2a2e,#6a4a3a 55%,#3a5a78)"></div>
    <div class="blog-date">05<br>Apr</div>
    <h3 class="blog-title">Lorem Ipsum is simply dummy text of the printing</h3>
    <p class="blog-excerpt">Lorem Ipsum is simply dummy text of the printing and typesetting industry.</p>
  </article>

  <article class="blog-card" style="left:434px">
    <div class="blog-image" role="img" aria-label="London riverside skyline at dusk with a bridge and a glass dome building" style="background:linear-gradient(180deg,#1d3f8a,#3a6cc0 50%,#2a3042)"></div>
    <div class="blog-date">05<br>Apr</div>
    <h3 class="blog-title">Lorem Ipsum is simply dummy text of the printing</h3>
    <p class="blog-excerpt">Lorem Ipsum is simply dummy text of the printing and typesetting industry.</p>
  </article>

  <article class="blog-card" style="left:790px">
    <div class="blog-image" role="img" aria-label="Two business partners reviewing a tablet in a bright office" style="background:linear-gradient(135deg,#dfe8f2,#8aa6c4 55%,#4a6a90)"></div>
    <div class="blog-date">05<br>Apr</div>
    <h3 class="blog-title">Lorem Ipsum is simply dummy text of the printing</h3>
    <p class="blog-excerpt">Lorem Ipsum is simply dummy text of the printing and typesetting industry.</p>
  </article>
</section>

<footer class="site-footer">
  <div class="footer-brand">
    <span class="brand-mark"></span>
    <span class="brand-name">bryn calvo</span>
  </div>
  <p class="footer-about">Lorem Ipsum is simply dummy text of the printing and typesetting industry.</p>

  <h4 class="footer-heading" style="left:435px">Contact Info</h4>
  <ul class="contact-list">
    <li style="top:0">
      <svg width="20" height="18" viewBox="0 0 20 18" fill="none" stroke="#fff" stroke-width="1.5"><path d="M1 3l6-2 6 2 6-2v14l-6 2-6-2-6 2z M7 1v14 M13 3v14"/></svg>
      123, Lorem ipsum dummy text,<br>Country – 123456.
    </li>
    <li style="top:62px">
      <svg width="20" height="20" viewBox="0 0 20 20" fill="none" stroke="#fff" stroke-width="1.5"><path d="M4 1l4 4-2 3c1 3 3 5 6 6l3-2 4 4-3 3C8 19 1 12 1 4z"/></svg>
      123 456 7878
    </li>
    <li style="top:104px">
      <svg width="20" height="16" viewBox="0 0 20 16" fill="none" stroke="#fff" stroke-width="1.5"><rect x="1" y="1" width="18" height="14"/><path d="M1 1l9 8 9-8"/></svg>
      info@bryncalvo.com
    </li>
  </ul>

  <h4 class="footer-heading" style="left:792px">Subscribe</h4>
  <p class="subscribe-text">Sign up to get updates about news &amp; Blogs of technology around London</p>
  <form class="subscribe-form">
    <input class="subscribe-input" type="email" placeholder="Enter E-Mail Address">
    <button class="subscribe-button" type="button">SIGN UP</button>
  </form>
</footer>

<div class="legal-bar">
  <p class="legal-text">© <strong>bryn calvo</strong> 2018. All Rights Reserved</p>
  <div class="social-links" aria-label="Social links">
    <span></span><span></span><span></span><span></span>
  </div>
</div>

</body>
</html>
```